Startup internet service provider needs door hanger and post card design

We are a startup internet service provider in Colorado, and we need some marketing materials. We provide internet service to home and business. This is a competitive market so we need something that will catch our potential customers eye. Brookvale Networks offers fast and reliable internet service without the headaches. No long term contracts or special promotions that expire and raise your rate. We offer a simple monthly rate with bills and features that are easy to understand.

Target Market(s)

Home and business internet subscribers

Colors
0555a3
acd036

Requirements
Must have
• Simple and professional
reference to website
https://brookvale-networks.example/
Nice to have
• qr code scan for website

```html
<!DOCTYPE html>
<html lang="en">
<head>
<meta charset="utf-8">
<title>Brookvale Networks Door Hanger</title>
<link rel="stylesheet" href="https://fonts.googleapis.com/css2?family=Barlow+Semi+Condensed:wght@600;700&family=Open+Sans:wght@400;700&family=Source+Sans+3:wght@400;600&display=swap">
<style>
  :root {
    --brand-blue: #0555a3;
    --brand-green: #acd036;
    --navy: #0a2a66;
    --ink: #222222;
    --paper: #ffffff;
    --backdrop: #f3f3f3;
    --body-text: #2f3a4a;
  }
  * { margin: 0; padding: 0; box-sizing: border-box; }
  html, body { width: 1200px; height: 2506px; overflow: hidden; }
  body { background: var(--backdrop); font-family: "Source Sans 3", sans-serif; }

  .door-hanger {
    position: absolute; left: 120px; top: 86px;
    width: 960px; height: 2334px;
    background: var(--paper);
    box-shadow: 0 10px 30px rgba(0,0,0,0.18);
    overflow: hidden;
  }
  .hanger-top { position: absolute; left: 0; top: 0; width: 960px; height: 500px; }

  .brand-line {
    position: absolute; top: 540px; left: 0; width: 100%;
    display: flex; justify-content: center; align-items: center; gap: 20px;
  }
  .brand-dot { width: 64px; height: 64px; border-radius: 50%; background: var(--brand-green); }
  .brand-name {
    font-family: "Source Sans 3", sans-serif; font-weight: 400;
    font-size: 54px; color: var(--brand-blue);
  }

  .family-photo {
    position: absolute; top: 658px; left: 0; width: 960px; height: 446px;
    background: linear-gradient(135deg, #e9e2d6 0%, #c9b79d 45%, #4a5670 70%, #d8cfc2 100%);
  }

  .headline {
    position: absolute; top: 1118px; left: 0; width: 100%; text-align: center;
    font-family: "Barlow Semi Condensed", sans-serif; font-weight: 700;
    font-size: 104px; line-height: 92px; color: var(--brand-blue);
  }
  .subhead {
    position: absolute; top: 1322px; left: 0; width: 100%; text-align: center;
    font-family: "Open Sans", sans-serif; font-weight: 700;
    font-size: 41px; color: var(--ink);
  }

  .intro-band {
    position: absolute; top: 1400px; left: 0; width: 960px; height: 230px;
    background: var(--brand-blue); color: var(--paper);
    padding: 10px 60px 0 66px;
    font-size: 32px; line-height: 41px;
  }

  .feature-list {
    position: absolute; top: 1684px; left: 64px; width: 850px;
    display: grid; grid-template-columns: 434px 1fr; column-gap: 0;
    list-style: none;
  }
  .feature-col { list-style: none; }
  .feature-col li {
    position: relative; padding-left: 34px; margin-bottom: 20px;
    font-size: 32px; line-height: 40px; color: var(--body-text);
  }
  .feature-col li svg { position: absolute; left: 0; top: 10px; width: 20px; height: 20px; }

  .contact-footer { position: absolute; left: 0; top: 2034px; width: 960px; height: 300px; }
  .contact-pill {
    position: absolute; top: 2040px; left: 308px; width: 344px; height: 62px;
    border-radius: 31px; background: var(--brand-blue); color: var(--paper);
    font-size: 32px; line-height: 62px; text-align: center; z-index: 2;
  }
  .phone-number {
    position: absolute; top: 2116px; left: 0; width: 100%; text-align: center;
    font-family: "Barlow Semi Condensed", sans-serif; font-weight: 700;
    font-size: 112px; line-height: 120px; color: var(--brand-blue);
  }
  .web-address {
    position: absolute; top: 2222px; left: 0; width: 100%; text-align: center;
    font-size: 44px; color: var(--brand-blue);
  }
</style>
</head>
<body>
<main class="door-hanger">
  <svg class="hanger-top" viewBox="0 0 960 500">
    <defs>
      <linearGradient id="fiberTone" x1="0" y1="0" x2="0" y2="1">
        <stop offset="0" stop-color="#0b1f4d"/>
        <stop offset="0.45" stop-color="#1f7cc4"/>
        <stop offset="1" stop-color="#0a2f73"/>
      </linearGradient>
    </defs>
    <path role="img" aria-label="Glowing blue fiber optic strands" d="M0 0 H960 V350 Q480 638 0 350 Z" fill="url(#fiberTone)"/>
    <path d="M0 350 Q480 638 960 350" fill="none" stroke="var(--brand-blue)" stroke-width="8"/>
    <path class="hanger-slot" d="M0 190 C160 170 380 140 500 160 L500 330 C380 350 160 300 0 262 Z" fill="var(--paper)"/>
    <circle class="hanger-hole" cx="638" cy="244" r="156" fill="var(--paper)"/>
  </svg>

  <div class="brand-line">
    <span class="brand-dot"></span>
    <span class="brand-name">Brookvale Networks</span>
  </div>

  <div class="family-photo" role="img" aria-label="Family sitting on a sofa using a laptop together"></div>

  <h1 class="headline">Fast and Reliable<br>Internet Service</h1>
  <p class="subhead">designed and catered to meet your needs</p>

  <p class="intro-band">Brookvale Networks offers fast and reliable internet service without the headaches. No long term contracts or special promotions that expire and raise your rate. We offer a simple monthly rate with bills and features that are easy to understand.</p>

  <div class="feature-list">
    <ul class="feature-col">
      <li><svg viewBox="0 0 20 20"><rect x="1.5" y="3.5" width="15" height="15" fill="none" stroke="var(--brand-blue)" stroke-width="2.5"/><path d="M5 10 L9 14 L18 3" fill="none" stroke="var(--brand-blue)" stroke-width="3"/></svg>Fast and reliable internet service</li>
      <li><svg viewBox="0 0 20 20"><rect x="1.5" y="3.5" width="15" height="15" fill="none" stroke="var(--brand-blue)" stroke-width="2.5"/><path d="M5 10 L9 14 L18 3" fill="none" stroke="var(--brand-blue)" stroke-width="3"/></svg>Real customer support</li>
      <li><svg viewBox="0 0 20 20"><rect x="1.5" y="3.5" width="15" height="15" fill="none" stroke="var(--brand-blue)" stroke-width="2.5"/><path d="M5 10 L9 14 L18 3" fill="none" stroke="var(--brand-blue)" stroke-width="3"/></svg>Less buffering while streaming</li>
      <li><svg viewBox="0 0 20 20"><rect x="1.5" y="3.5" width="15" height="15" fill="none" stroke="var(--brand-blue)" stroke-width="2.5"/><path d="M5 10 L9 14 L18 3" fill="none" stroke="var(--brand-blue)" stroke-width="3"/></svg>Fast web browsing</li>
    </ul>
    <ul class="feature-col">
      <li><svg viewBox="0 0 20 20"><rect x="1.5" y="3.5" width="15" height="15" fill="none" stroke="var(--brand-blue)" stroke-width="2.5"/><path d="M5 10 L9 14 L18 3" fill="none" stroke="var(--brand-blue)" stroke-width="3"/></svg>Gaming without the lag</li>
      <li><svg viewBox="0 0 20 20"><rect x="1.5" y="3.5" width="15" height="15" fill="none" stroke="var(--brand-blue)" stroke-width="2.5"/><path d="M5 10 L9 14 L18 3" fill="none" stroke="var(--brand-blue)" stroke-width="3"/></svg>Wall to wall WiFi coverage</li>
      <li><svg viewBox="0 0 20 20"><rect x="1.5" y="3.5" width="15" height="15" fill="none" stroke="var(--brand-blue)" stroke-width="2.5"/><path d="M5 10 L9 14 L18 3" fill="none" stroke="var(--brand-blue)" stroke-width="3"/></svg>No introductory charges, one constant rate</li>
      <li><svg viewBox="0 0 20 20"><rect x="1.5" y="3.5" width="15" height="15" fill="none" stroke="var(--brand-blue)" stroke-width="2.5"/><path d="M5 10 L9 14 L18 3" fill="none" stroke="var(--brand-blue)" stroke-width="3"/></svg>Simple and easy to read bills</li>
    </ul>
  </div>

  <svg class="contact-footer" viewBox="0 0 960 300">
    <path d="M0 120 Q480 -28 960 120 V300 H0 Z" fill="var(--brand-green)"/>
    <path d="M0 120 Q480 -28 960 120" fill="none" stroke="var(--brand-blue)" stroke-width="7"/>
  </svg>
  <div class="contact-pill">CONTACT US</div>
  <p class="phone-number">844-555-0192</p>
  <p class="web-address">www.brookvale-networks.example</p>
</main>
</body>
</html>
```